business card for LWR pty ltd

We require a business card that stands out . I have included our company flyer and would like the services listed to be put on the card so when we Give out the cards to customers they have an idea of services we provide. need the winning design to be in editable photo shop format, editable iMac pages format or editable windows publisher format, so that I can enter in names, email addresses, phone numbers etc myself. I have included a pdf documents of info / items needed on the card to use as reference please.
Updates

need more submissions

Need extra days to review

Sick

Target Market(s)

new customers

Contact Information for Business Card

details are on attached business card requirements file

Requirements
Must have
• I have attached a list of must haves

```html
<!DOCTYPE html>
<html lang="en">
<head>
<meta charset="utf-8">
<title>LWR Pty Ltd – Business Card</title>
<link rel="stylesheet" href="https://fonts.googleapis.com/css2?family=Open+Sans:wght@400;700;800&display=swap">
<style>
  :root {
    --page-bg: #2a2f36;
    --card-black: #0b0b0b;
    --card-charcoal: #1c1c1c;
    --frame-line: #bfbfbf;
    --text-white: #ffffff;
    --text-soft: #e6e6e6;
    --gold-light: #8f7140;
    --gold-mid: #5d4623;
    --gold-dark: #141008;
    --mark-silver: #b9b9b9;
    --photo-sand: rgba(184,135,92,.85);
    --photo-truck: rgba(58,61,64,.6);
  }
  html, body {
    margin: 0;
    width: 1200px;
    height: 900px;
    overflow: hidden;
    background: var(--page-bg);
    font-family: "Open Sans", Arial, sans-serif;
  }
  .card {
    position: absolute;
    left: 240px;
    width: 720px;
    height: 410px;
    overflow: hidden;
    box-shadow: 0 10px 30px rgba(0,0,0,.45);
  }
  .card-frame {
    position: absolute;
    inset: 14px;
    border: 1.5px solid var(--frame-line);
    pointer-events: none;
  }

  /* Front */
  .card-front {
    top: 30px;
    background: var(--card-black);
  }
  .front-glow {
    position: absolute;
    left: 30px; top: 20px;
    width: 330px; height: 240px;
    background: radial-gradient(ellipse at center, #3a3a3a 0%, var(--card-charcoal) 45%, var(--card-black) 75%);
  }
  .front-mark {
    position: absolute;
    left: 80px; top: 80px;
    display: flex;
    align-items: center;
    gap: 14px;
    font-weight: 800;
    font-size: 84px;
    letter-spacing: 2px;
    color: var(--mark-silver);
  }
  .mark-dot {
    width: 22px; height: 22px;
    border-radius: 50%;
    background: var(--mark-silver);
  }
  .front-photo {
    position: absolute;
    left: 120px; top: 240px;
    width: 240px; height: 150px;
    background: radial-gradient(ellipse at 50% 55%, #c9c6bd 0%, #7b705b 40%, #2c2820 70%, var(--card-black) 100%);
  }
  .front-details {
    position: absolute;
    left: 380px; top: 60px;
    color: var(--text-white);
  }
  .company-name {
    margin: 0;
    font-size: 40px;
    font-weight: 800;
    line-height: 1.1;
  }
  .person-name {
    margin: 8px 0 14px;
    font-size: 19px;
    font-weight: 700;
  }
  .contact-list {
    list-style: none;
    margin: 0; padding: 0;
    font-size: 15px;
    line-height: 1.65;
    color: var(--text-soft);
  }

  /* Back */
  .card-back {
    top: 465px;
    background: linear-gradient(180deg, var(--gold-light) 0%, var(--gold-mid) 35%, var(--gold-dark) 70%, var(--card-black) 100%);
  }
  .back-photo {
    position: absolute;
    left: 0; top: 170px;
    width: 620px; height: 240px;
    background:
      radial-gradient(ellipse 75% 55% at 35% 100%, var(--photo-sand) 0%, rgba(140,100,67,.5) 55%, rgba(0,0,0,0) 100%),
      radial-gradient(ellipse 70% 45% at 40% 35%, var(--photo-truck) 0%, rgba(0,0,0,0) 100%);
  }
  .back-mark {
    position: absolute;
    left: 250px; top: 200px;
    display: flex;
    align-items: center;
    gap: 12px;
    font-weight: 800;
    font-size: 56px;
    line-height: 1;
    color: var(--mark-silver);
  }
  .back-mark .mark-dot { width: 18px; height: 18px; }
  .service-list {
    position: absolute;
    margin: 0;
    padding-left: 18px;
    color: var(--text-white);
    font-weight: 700;
    font-size: 15px;
    line-height: 1.45;
  }
  .service-list li::marker { font-size: 18px; }
  .services-left { left: 40px; top: 30px; }
  .services-right { left: 478px; top: 200px; }
</style>
</head>
<body>

<section class="card card-front" aria-label="Business card front">
  <div class="front-glow"></div>
  <div class="front-mark"><span class="mark-dot"></span>LWR</div>
  <div class="front-photo" role="img" aria-label="Photo of two road train trucks, front view"></div>
  <div class="front-details">
    <h1 class="company-name">LWR Pty Ltd</h1>
    <p class="person-name">Daniel Harwood (Director)</p>
    <ul class="contact-list">
      <li>Depot: Lot 118 sample address Australia</li>
      <li>Email: email@lwrservices.com.au</li>
      <li>Phone: 000 555 000</li>
      <li>Website: www.websiteaddress.com</li>
    </ul>
  </div>
  <div class="card-frame"></div>
</section>

<section class="card card-back" aria-label="Business card back">
  <div class="back-photo" role="img" aria-label="Photo of a road train tipper on red dirt"></div>
  <div class="back-mark"><span class="mark-dot"></span>LWR</div>
  <ul class="service-list services-left">
    <li>Over size Loads / Hot shot Loads</li>
    <li>Havy vehicle recovery services</li>
    <li>Potable water deleveries</li>
    <li>Road building &amp; Maintanance</li>
    <li>Earthworks</li>
    <li>Sand &amp; Mettle Supply Cartage</li>
  </ul>
  <ul class="service-list services-right">
    <li>Road train tippers</li>
    <li>Road train tankers</li>
    <li>Road train flat tops</li>
    <li>Drop deck Trailers</li>
    <li>Mine site accredited</li>
    <li>Equipments &amp; Operetors</li>
  </ul>
  <div class="card-frame"></div>
</section>

</body>
</html>
```